Website design for headhunting agency

The design I need (PSD file) is for a company offering specialised services in recruitment of high-end executive and management positions for businesses.
OBJECTIVES OF THE WEBSITE:
1. Let entrepreneurs and business leaders know about their services and easily have them contact Velnarix if they want more information about their services.
2. Display a list of available carreer opportunities (according to their client's need).
WHAT I NEED:
1st, I need the design for the Home Page ONLY. Once approved, I will need the other pages designed as well. (Here is prototype that we've already developed for the Website that will guide you in the design:
http://demo.quorvaweb.example/velnarix/fr/accueil)
ATTACHED FILES
- Logo
- PDF brochure: Use for inspiration. It is encouraged that you use pictures from this brochure. You can always suggest new ones, as long as they are not expensive to buy and have the same look and feel as the brochure.
HOMEPAGE:
1. Main menu : 6 sections
Accueil | Velnarix | Équipe | Approche | Postes disponibles | Publications
2. Main slider: 4 sections
- Chasseurs de têtes (Headhunters)
- Notre approche (Our Approach)
- Postes cadres disponibles (Executive Careers
Opportunities)
- Contactez-nous (Contact Us)
3. Main Call To Action Boxes :
- Liste Des postes disponibles (Liste of Available Careers
Opportunities)
- Formulaire de contact (contact form)
4. Latest blog articles
- Les derniers articles.
OTHER PAGES (to design once Homepage is approved)
- Velnarix (about us)
- Équipe (our team)
- Approche (our approach)
- Postes disponibles (Career opportunities)
- Publications (blog articles)
- Contact (Contact us)
Target Market(s)
ORGANIZATIONS:
Leaders of organizations seeking to recruit highly qualified staff.
HIGHLY QUALIFIED RESOURCES:
Senior individuals seeking a salary between $70,000 and $ $200,000 annually
PROFESSIONAL SECTORS:
manufacturing : Primary and secondary industries
pharmaceutical
Aerospace
Finances
Retail business
Engineering
Chemical and petrochemical
IT, telecommunications and high technology
Professional Organizations and Association
Industry/Entity Type
Business
Look and feel
Each slider illustrates characteristics of the customer's brand and the style your logo design should communicate.

```html
<!DOCTYPE html>
<html lang="fr">
<head>
<meta charset="utf-8">
<title>Velnarix – Recherche de cadres</title>
<link href="https://fonts.googleapis.com/css2?family=Arimo:wght@400;700&display=swap" rel="stylesheet">
<style>
:root{
  --teal-dark:#3d7281;
  --teal-text:#1f5d6c;
  --heading:#3f7d92;
  --link:#4f8aa3;
  --gold:#d9a418;
  --pale:#e8f0f5;
  --card-bg:#eaf1f6;
  --card-line:#c8d7e1;
  --body:#3a3a3a;
  --muted:#7a7a7a;
  --white:#ffffff;
}
*{margin:0;padding:0;box-sizing:border-box}
html,body{width:996px;height:1200px;overflow:hidden;background:var(--pale)}
body{font-family:'Arimo',Arial,sans-serif;color:var(--body)}
.page{width:1200px;height:1446px;transform:scale(0.83);transform-origin:0 0;position:relative;background:var(--pale)}
.abs{position:absolute}

/* top bar */
.topbar{top:0;left:0;width:1200px;height:42px;background:var(--teal-dark)}
.topbar ul{list-style:none;display:flex;position:absolute;right:100px;top:0;height:42px}
.topbar li{color:var(--white);font-size:13px;font-weight:700;padding:0 11px;line-height:42px;border-left:1px solid rgba(255,255,255,.18)}
.topbar li:first-child{border-left:none}
.topbar .lang::after{content:"";display:inline-block;margin-left:6px;border:5px solid transparent;border-top:8px solid #b8cfd6;border-bottom:0;vertical-align:middle}

/* header */
.header{top:42px;left:0;width:1200px;height:93px;background:var(--pale)}
.brand{left:105px;top:12px}
.brand-mark{width:14px;height:14px;background:var(--gold);position:absolute;left:83px;top:4px}
.brand-name{position:absolute;left:0;top:26px;font-size:27px;color:var(--teal-text);letter-spacing:1px;font-weight:400}
.brand-tag{position:absolute;left:66px;top:54px;font-size:11px;color:#777;white-space:nowrap}
.mainnav{right:90px;top:0;height:93px;display:flex;list-style:none}
.mainnav li{font-size:12.5px;font-weight:700;color:#2d4f5b;line-height:98px;padding:0 13px;border-left:1px solid #d6e2e9}
.mainnav li:first-child{border-left:none;color:var(--gold)}

/* hero */
.hero{top:135px;left:0;width:1200px;height:375px;background:linear-gradient(100deg,#3f6c84 0%,#5a8da3 30%,#8fbfcf 55%,#63aab5 80%,#2c8b92 100%);overflow:hidden}
.hero-facet{top:0;left:0;width:1200px;height:375px}
.hero-photo{right:180px;top:25px;width:290px;height:350px;background:radial-gradient(ellipse at 50% 40%,#e6eef2 0%,#c9dbe3 45%,rgba(150,195,210,0) 75%)}
.hero h1{left:138px;top:86px;font-size:26px;color:var(--white);font-weight:700;letter-spacing:.3px}
.hero p{left:140px;top:124px;width:360px;font-size:12px;line-height:19px;color:var(--white)}
.know{left:143px;top:210px;display:flex;align-items:center;color:var(--white);font-size:12.5px;font-weight:700}
.know svg{margin-left:15px}
.dots{left:146px;top:332px;display:flex;gap:10px}
.dots span{width:11px;height:11px;border-radius:50%;background:#a9d6ea}

/* call to action cards */
.card{background:var(--white);border-bottom:4px solid #8fb4c6;box-shadow:0 0 4px rgba(0,0,0,.08)}
.card h2{position:absolute;left:21px;top:14px;font-size:14.5px;color:var(--heading);font-weight:700;letter-spacing:.2px}
.jobs{left:143px;top:550px;width:440px;height:229px}
.job{position:absolute;left:41px;width:378px}
.job::before{content:"";position:absolute;left:-18px;top:6px;width:7px;height:1px;background:#333}
.job::after{content:"";position:absolute;left:-13px;top:4px;border:2.5px solid transparent;border-left:4px solid #333}
.job h3{font-size:12px;color:var(--link);font-weight:700}
.job p{font-size:12px;color:var(--muted);line-height:17px;margin-top:5px}
.job p span{color:var(--teal-text)}
.job-1{top:51px;padding-bottom:12px;border-bottom:1px solid #e3e3e3}
.job-2{top:132px}
.viewall{left:41px;top:198px;font-size:12px;color:var(--teal-text);font-weight:700}
.contact{left:614px;top:550px;width:454px;height:229px}
.field{position:absolute;border:1px solid #c5c5c5;background:var(--white);font-size:11.5px;color:#aaa;padding:11px 12px}
.submit{position:absolute;left:304px;top:143px;width:69px;height:66px;background:linear-gradient(#2e2e2e,#6b6b6b);color:var(--white);font-size:12px;font-weight:700;padding:19px 11px;line-height:17px}

/* articles */
.articles{top:822px;left:0;width:1200px;height:408px;background:var(--white)}
.articles h2{position:absolute;top:29px;width:1200px;text-align:center;font-size:15.5px;color:var(--heading);font-weight:700}
.post{position:absolute;background:var(--card-bg);border:1px solid var(--card-line)}
.post .thumb{position:absolute;left:7px;top:10px;width:126px;height:117px;border:2px solid #d7e0e6}
.post h3{position:absolute;left:152px;top:12px;font-size:13px;color:var(--teal-text);font-weight:700}
.post p{position:absolute;left:152px;top:38px;width:270px;font-size:12px;line-height:18px;color:var(--body)}
.post .more{position:absolute;left:152px;top:93px;font-size:13px;color:var(--gold);font-weight:700}

/* follow banners */
.banner{position:absolute;top:1268px;width:440px;height:78px;background:linear-gradient(90deg,#3c7283 0%,#5b98b0 50%,#7bbad7 100%);border:1px solid #d5e3ea;color:var(--white);font-size:16px;font-weight:700}
.banner span{position:absolute;top:28px}

/* footer */
.footer{top:1388px;left:0;width:1200px;height:52px;background:var(--teal-dark)}
.footer .copy{position:absolute;left:148px;top:19px;font-size:12px;color:var(--white)}
.footer .count{position:absolute;left:937px;top:20px;font-size:12px;color:var(--white)}
.social{position:absolute;top:8px;width:33px;height:33px;border-radius:50%;border:2px solid rgba(255,255,255,.25)}
</style>
</head>
<body>
<div class="page">

  <div class="abs topbar">
    <ul>
      <li>Accueil</li><li>Plan du site</li><li>Code d'étique</li><li>Contact</li><li class="lang">English</li>
    </ul>
  </div>

  <header class="abs header">
    <div class="abs brand">
      <span class="brand-mark"></span>
      <span class="brand-name">VELNARIX</span>
      <span class="brand-tag">Recherche de cadres</span>
    </div>
    <ul class="abs mainnav">
      <li>ACCUEIL</li><li>VELNARIX</li><li>ÉQUIPE</li><li>APPROCHE</li><li>POSTES DISPONIBLES</li><li>PUBLICATIONS</li>
    </ul>
  </header>

  <section class="abs hero">
    <svg class="abs hero-facet" viewBox="0 0 1200 375" aria-hidden="true">
      <polygon points="0,0 330,0 130,375 0,375" fill="#2f5c75" opacity=".35"/>
      <polygon points="330,375 560,0 620,0 420,375" fill="#ffffff" opacity=".06"/>
      <polygon points="1200,0 1200,375 1060,375" fill="#1f7f86" opacity=".35"/>
    </svg>
    <div class="abs hero-photo" role="img" aria-label="Portrait photo of a smiling businesswoman in a light jacket, arms crossed"></div>
    <h1 class="abs">CHASSEURS DE TÊTES</h1>
    <p class="abs">Doloremque laudantium, totam rem eaque ipsa quae ab illo inven-tore veritatis et quasi architecto beaae vitae dict a sunt explicabo. Nemo enim ipvoluptatem quia voluptas sit aspernatur aut odit aut fugit, sed quia consequuntur magni dolores eos qui ration</p>
    <div class="abs know">KNOW MORE
      <svg width="24" height="24" viewBox="0 0 24 24" aria-hidden="true"><circle cx="12" cy="12" r="12" fill="#fff"/><path d="M10 7l5 5-5 5" stroke="#3d6274" stroke-width="2.6" fill="none"/></svg>
    </div>
    <div class="abs dots"><span></span><span></span><span></span><span></span></div>
  </section>

  <section class="abs card jobs">
    <h2>LISTE DES POSTES DISPONIBLES</h2>
    <div class="job job-1">
      <h3>Doloremque laudantium, totam rem eaque ipsa</h3>
      <p>Aaudantium, totam rem eaque ipsa quae ab illo inventore<br>quasi archite &nbsp;| &nbsp;<span>APPLY</span></p>
    </div>
    <div class="job job-2">
      <h3>Doloremque laudantium, totam rem eaque ipsa</h3>
      <p>Aaudantium, totam rem eaque ipsa quae ab illo inventore<br>quasi archite &nbsp;| &nbsp;<span>APPLY</span></p>
    </div>
    <div class="abs viewall">View All</div>
  </section>

  <section class="abs card contact">
    <h2>FORMULAIRE DE CONTACT</h2>
    <div class="field" style="left:26px;top:48px;width:163px;height:36px">Name</div>
    <div class="field" style="left:207px;top:48px;width:163px;height:36px">Email</div>
    <div class="field" style="left:27px;top:96px;width:163px;height:36px">Phone</div>
    <div class="field" style="left:208px;top:96px;width:163px;height:36px">Company</div>
    <div class="field" style="left:27px;top:142px;width:264px;height:66px">Your Message</div>
    <div class="submit">SUBMIT<br>NOW</div>
  </section>

  <section class="abs articles">
    <h2>LES DERNIERS ARTICLES</h2>
    <article class="post" style="left:144px;top:76px;width:439px;height:138px">
      <div class="thumb" role="img" aria-label="Photo of a modern interior with glass partitions" style="background:linear-gradient(135deg,#c9b98e,#6b5a3c 60%,#3f7fa8)"></div>
      <h3>Doloremque laudantium, totam rem eaque</h3>
      <p>Sed ut perspiciatis unde omnis iste natus error sit voluptatem accusantium doloremque perspiciatis unde omnis iste natus error sit</p>
      <span class="more">Read more..</span>
    </article>
    <article class="post" style="left:615px;top:76px;width:443px;height:139px">
      <div class="thumb" role="img" aria-label="Photo of a woman holding a small house model" style="background:linear-gradient(160deg,#e7e5e0,#a88a72 55%,#8c8f92)"></div>
      <h3 style="left:162px">Doloremque laudantium, totam rem eaque</h3>
      <p style="left:162px">Sed ut perspiciatis unde omnis iste natus error sit voluptatem accusantium doloremque perspiciatis unde omnis iste natus error sit</p>
      <span class="more" style="left:162px">Read more..</span>
    </article>
    <article class="post" style="left:143px;top:239px;width:440px;height:136px">
      <div class="thumb" role="img" aria-label="Photo of smiling colleagues in a meeting" style="background:linear-gradient(120deg,#f0ece8,#b59785 50%,#d8d6d4)"></div>
      <h3>Doloremque laudantium, totam rem eaque</h3>
      <p style="left:150px">Sed ut perspiciatis unde omnis iste natus error sit voluptatem accusantium doloremque perspiciatis unde omnis iste natus error sit</p>
      <span class="more" style="left:150px">Read more..</span>
    </article>
    <article class="post" style="left:615px;top:239px;width:443px;height:136px">
      <div class="thumb" role="img" aria-label="Photo of a team raising thumbs up" style="background:linear-gradient(135deg,#6f9bc3,#d8b8a0 50%,#3e6f9e)"></div>
      <h3 style="left:156px;top:9px">Doloremque laudantium, totam rem eaque</h3>
      <p style="left:157px;top:35px">Sed ut perspiciatis unde omnis iste natus error sit voluptatem accusantium doloremque perspiciatis unde omnis iste natus error sit</p>
      <span class="more" style="left:157px;top:90px">Read more..</span>
    </article>
  </section>

  <div class="banner" style="left:146px">
    <svg class="abs" style="left:61px;top:21px" width="30" height="30" aria-hidden="true"><rect width="30" height="30" rx="3" fill="#2a9bd4"/></svg>
    <span style="left:116px">Suivez-nous sur Linkora</span>
  </div>
  <div class="banner" style="left:616px">
    <svg class="abs" style="left:46px;top:19px" width="32" height="30" viewBox="0 0 32 30" aria-hidden="true">
      <rect x="1" y="6" width="30" height="22" rx="2" fill="#e9eef1" stroke="#c9d3d8"/>
      <rect x="6" y="1" width="20" height="16" fill="#ffffff"/>
      <path d="M1 8l15 11 15-11" stroke="#2a8fc9" stroke-width="2" fill="none"/>
    </svg>
    <span style="left:105px">Inscrivez-vous à l'infolettre</span>
  </div>

  <footer class="abs footer">
    <span class="copy">© Velnarix - Tous droits réservés</span>
    <span class="count">X5</span>
    <span class="social" style="left:962px;background:#3b5b9a"></span>
    <span class="social" style="left:998px;background:#d8312f"></span>
    <span class="social" style="left:1034px;background:#3fa6dd"></span>
  </footer>

</div>
</body>
</html>
```